Stationery Required - Own Logo provided

Hi,

We are a retail company called 'Copperfinch Trading Limited' based in the UK and would like some corporate stationery designed.

We have provided our Logo which we would like to use (Its attached to this brief)...

The designs must be orginal, professional, stylish and interesting!

Target Market(s)

We will use this stationery to communicate with our wholesale suppliers and employees, so it must have a 'professional' feel about it.

Industry/Entity Type

It Company

Requirements
Must have
• Must be professional, corporate, stylish and not to 'fussy'. we require ... Business card design, a4 letter, compliment slip. All designs must be supplied in a format where the text (address/telephone numbers etc..) can be edited, as we have alot of staff and operate out of several different premises.
Nice to have
• I would like a windows backround picture file supplied as well so we can integrate that onto our computer systems.

```html
<!DOCTYPE html>
<html lang="en">
<head>
<meta charset="utf-8">
<title>Copperfinch Trading Limited – Stationery</title>
<link rel="stylesheet" href="https://fonts.googleapis.com/css2?family=Questrial&display=swap">
<style>
  :root {
    --lime: #9fd21e;
    --lime-light: #c6e67a;
    --lime-pale: #e3f2c2;
    --leaf: #5a8a1a;
    --forest: #3f6b13;
    --ink: #1b1d19;
    --charcoal: #2b2e28;
    --paper: #ffffff;
    --backdrop: #ecebe6;
    --grey-text: #4a4d47;
  }
  * { box-sizing: border-box; margin: 0; padding: 0; }
  html, body { width: 1200px; height: 815px; overflow: hidden; }
  body {
    background: var(--backdrop);
    font-family: "Questrial", "Century Gothic", sans-serif;
    position: relative;
  }
  .piece { position: absolute; overflow: hidden; }

  /* brand name (stands where the mark would be) */
  .brand { display: flex; align-items: center; gap: 6px; white-space: nowrap; }
  .brand-square { width: 12px; height: 12px; background: var(--forest); flex: none; }
  .brand-name { color: var(--forest); font-size: 14px; letter-spacing: .2px; }

  /* ---------- business card fronts ---------- */
  .card-front { background: linear-gradient(135deg, var(--charcoal), var(--ink)); width: 325px; z-index: 2; }
  .card-front--square { left: 20px; top: 30px; height: 200px; }
  .card-front--round { left: 20px; top: 395px; height: 190px; border-radius: 18px; }
  .card-front .band { position: absolute; left: 210px; right: 0; top: 70px; height: 65px; background: var(--lime); }
  .card-front .stripe { position: absolute; left: 128px; width: 18px; top: 120px; bottom: 0; background: var(--leaf); }
  .card-front .glow-square {
    position: absolute; left: 112px; top: 58px; width: 98px; height: 98px;
    background: var(--paper); box-shadow: 0 0 18px 8px rgba(240,255,200,.75);
  }
  .card-front .brand { position: absolute; right: 12px; bottom: 14px; }
  .card-front .brand-name { color: var(--lime); font-size: 16px; }

  /* ---------- business card backs ---------- */
  .card-back { background: var(--paper); box-shadow: 0 4px 14px rgba(0,0,0,.25); z-index: 1; }
  .card-back--square { left: 202px; top: 202px; width: 305px; height: 178px; }
  .card-back--round { left: 200px; top: 555px; width: 307px; height: 175px; border-radius: 16px; }
  .card-back .name-band {
    position: absolute; left: 0; top: 78px; width: 160px; height: 26px;
    background: var(--lime-pale); padding-left: 8px; display: flex; align-items: center; gap: 4px;
  }
  .card-back .name-band .brand-name { font-size: 9px; letter-spacing: 0; }
  .card-back .name-band .brand-square { width: 9px; height: 9px; }
  .card-back .contact-panel {
    position: absolute; left: 160px; top: 0; right: 0; bottom: 0;
    background: var(--lime-pale); text-align: center; padding-top: 94px;
    color: var(--leaf); font-size: 8px; line-height: 1.25;
  }
  .card-back .contact-panel .faint-square {
    position: absolute; left: 36px; top: 10px; width: 74px; height: 74px; background: var(--lime-light); opacity: .55;
  }
  .person-name { color: var(--grey-text); font-size: 11px; }
  .person-role { color: var(--grey-text); font-size: 8px; margin-bottom: 2px; }
  .contact-address { margin-top: 6px; font-style: italic; }

  /* ---------- letterhead ---------- */
  .letterhead { left: 520px; top: 30px; width: 482px; height: 700px; background: var(--paper); box-shadow: 0 4px 16px rgba(0,0,0,.2); }
  .letterhead svg { position: absolute; inset: 0; }
  .letterhead .brand { position: absolute; right: 10px; top: 18px; }
  .letterhead .faint-square { position: absolute; right: 12px; top: 575px; width: 92px; height: 88px; background: var(--lime-light); opacity: .6; }
  .letterhead .footer { position: absolute; left: 14px; bottom: 10px; color: var(--paper); font-size: 8px; line-height: 1.55; }

  /* ---------- envelope ---------- */
  .envelope {
    left: 733px; top: 185px; width: 437px; height: 245px;
    background: linear-gradient(180deg, var(--paper) 10%, var(--lime-pale) 45%, var(--lime) 100%);
    box-shadow: 0 4px 16px rgba(0,0,0,.25);
  }
  .envelope .flap { position: absolute; left: 0; right: 0; top: 0; height: 37px; background: linear-gradient(180deg, var(--lime), #b5dd3e); }
  .envelope .faint-square { position: absolute; left: 262px; top: 45px; width: 160px; height: 190px; background: var(--lime-light); opacity: .55; }
  .envelope .brand { position: absolute; left: 20px; top: 52px; }
  .envelope .brand-name { font-size: 16px; }
  .envelope .window { position: absolute; left: 254px; top: 140px; width: 150px; height: 73px; background: var(--paper); }
</style>
</head>
<body>

  <!-- business card, square corners -->
  <div class="piece card-front card-front--square">
    <div class="band"></div>
    <div class="stripe"></div>
    <div class="glow-square"></div>
    <div class="brand"><span class="brand-name">Copperfinch Trading Limited</span></div>
  </div>
  <div class="piece card-back card-back--square">
    <div class="name-band brand"><span class="brand-square"></span><span class="brand-name">Copperfinch Trading Limited</span></div>
    <div class="contact-panel">
      <div class="faint-square"></div>
      <p class="person-name">Martin Keel</p>
      <p class="person-role">Director</p>
      <p>07700900461</p>
      <p>office@copperfinch.co.uk</p>
      <p class="contact-address">17 Mill Lane, Ashbourne,<br>County Down BT30 4QP</p>
    </div>
  </div>

  <!-- business card, rounded corners -->
  <div class="piece card-front card-front--round">
    <div class="band"></div>
    <div class="stripe"></div>
    <div class="glow-square"></div>
    <div class="brand"><span class="brand-name">Copperfinch Trading Limited</span></div>
  </div>
  <div class="piece card-back card-back--round">
    <div class="name-band brand"><span class="brand-square"></span><span class="brand-name">Copperfinch Trading Limited</span></div>
    <div class="contact-panel">
      <div class="faint-square"></div>
      <p class="person-name">Martin Keel</p>
      <p class="person-role">Director</p>
      <p>07700900461</p>
      <p>office@copperfinch.co.uk</p>
      <p class="contact-address">17 Mill Lane, Ashbourne,<br>County Down BT30 4QP</p>
    </div>
  </div>

  <!-- A4 letterhead -->
  <div class="piece letterhead">
    <svg width="482" height="700" viewBox="0 0 482 700" aria-hidden="true">
      <path d="M0,0 H482 V135 C360,118 160,70 10,0 Z" fill="#9fd21e"/>
      <path d="M0,0 H482 V105 C360,92 170,50 40,0 Z" fill="#c6e67a" opacity=".8"/>
      <path d="M0,0 H482 V75 C370,66 200,34 90,0 Z" fill="#e3f2c2" opacity=".9"/>
      <path d="M0,600 C150,602 330,640 450,700 H0 Z" fill="#c6e67a" opacity=".7"/>
      <path d="M0,622 C150,626 320,660 420,700 H0 Z" fill="#9fd21e"/>
    </svg>
    <div class="brand"><span class="brand-square"></span><span class="brand-name">Copperfinch Trading Limited</span></div>
    <div class="faint-square"></div>
    <div class="footer">
      <p>07700900461</p>
      <p>office@copperfinch.co.uk</p>
      <p>17 Mill Lane, Ashbourne, County Down BT30 4QP</p>
    </div>
  </div>

  <!-- DL envelope -->
  <div class="piece envelope">
    <div class="flap"></div>
    <div class="faint-square"></div>
    <div class="brand"><span class="brand-square"></span><span class="brand-name">Copperfinch Trading Limited</span></div>
    <div class="window"></div>
  </div>

</body>
</html>
```